Business Cards that are elegant and wow

I want to create and print business cards that represent my brand and stand out from the rest. We want to ensure they stay in our branding and the integrity is not lost. I am happy to look at different shapes like square etc.

It will be printed on very thick cards and will be stylish .

I want to create and print business cards that represent my brand and stand out from the rest. We want to ensure they stay in ur branding and the integrity is not lost. I am happy to look at different shapes like square etc.

Target Market(s)

real estate professionals

Industry/Entity Type

Real Estate

Contact Information for Business Card

Maren Holt
hello@brightfernrealty.com.au
brightfernrealty.com.au
0487 316 252 (SMS)

Colors

Designer to choose colors to be used in the design.

Requirements
Must have
• My logo
• email
• website
• Name
Nice to have
• I like the idea of printing with foil or spot gloss. You want it to stand out in a sea.
Should not have
• I would like you to stay in my colour themes. Don't change the colour of my logo

```html
<!DOCTYPE html>
<html lang="en">
<head>
<meta charset="utf-8">
<title>Bright Fern Realty – Business Cards</title>
<link href="https://fonts.googleapis.com/css2?family=Montserrat:wght@600&family=Open+Sans:wght@300;600&display=swap" rel="stylesheet">
<style>
  :root {
    --backdrop: #e4e4e6;
    --card-dark: #0b0b0c;
    --card-light: #ffffff;
    --brand-pink: #e6197e;
    --brand-cyan: #1ea9e1;
    --contact-grey: #8a8a8e;
    --ring-faint: rgba(30, 169, 225, 0.16);
  }
  * { margin: 0; padding: 0; box-sizing: border-box; }
  html, body {
    width: 1200px; height: 800px; overflow: hidden;
    background: var(--backdrop);
  }
  .canvas {
    position: relative; width: 1200px; height: 800px;
    display: flex; align-items: center; justify-content: center; gap: 70px;
  }
  .card {
    position: relative; width: 500px; height: 286px; overflow: hidden;
    border-radius: 3px;
    box-shadow: 0 10px 26px rgba(0,0,0,0.14);
  }
  .card--back { background: var(--card-dark); }
  .card--front {
    background: var(--card-light);
    display: flex; align-items: center; justify-content: center;
  }
  .wordmark {
    display: flex; align-items: center; gap: 12px;
  }
  .wordmark__dot {
    width: 34px; height: 34px; border-radius: 50%;
    border: 3px solid var(--brand-pink);
    flex-shrink: 0;
  }
  .wordmark__name {
    font-family: "Montserrat", sans-serif; font-weight: 600;
    font-size: 26px; letter-spacing: 0.5px; text-transform: uppercase;
    color: var(--brand-cyan); line-height: 1;
  }
  .card--back .wordmark {
    position: absolute; left: 30px; top: 34px;
  }
  .card--back .wordmark__name { font-size: 24px; }
  .decor-ring {
    position: absolute; right: -40px; bottom: -120px;
    width: 300px; height: 300px; border-radius: 50%;
    border: 14px solid var(--ring-faint);
  }
  .holder {
    position: absolute; left: 30px; bottom: 34px;
  }
  .holder__name {
    font-family: "Open Sans", sans-serif; font-weight: 600;
    font-size: 15px; letter-spacing: 0.5px; text-transform: uppercase;
    color: var(--brand-pink); margin-bottom: 6px;
  }
  .holder__contact {
    font-family: "Open Sans", sans-serif; font-weight: 300;
    font-size: 11.5px; color: var(--contact-grey); white-space: nowrap;
  }
</style>
</head>
<body>
  <main class="canvas">
    <section class="card card--back" aria-label="Business card, back">
      <div class="decor-ring" aria-hidden="true"></div>
      <div class="wordmark">
        <span class="wordmark__dot" aria-hidden="true"></span>
        <span class="wordmark__name">Bright Fern Realty</span>
      </div>
      <div class="holder">
        <p class="holder__name">Maren Holt</p>
        <p class="holder__contact">0487 316 252 (SMS) | brightfernrealty.com.au | hello@brightfernrealty.com.au</p>
      </div>
    </section>

    <section class="card card--front" aria-label="Business card, front">
      <div class="wordmark">
        <span class="wordmark__dot" aria-hidden="true"></span>
        <span class="wordmark__name">Bright Fern Realty</span>
      </div>
    </section>
  </main>
</body>
</html>
```